Design for Poster ad for Cheerleading Gym

I need someone to design a poster type ad for my Cheerleading gym. The ad will be displayed in our local mall during the holiday season. I have attached photo, but have a higher resolution available. I have also attached the spec sheet. I would like the photo with the text "Soar" over it, at the top of the ad. The background to fade from a light color (blue?) at the top to black at the bottom. Text at the bottom to be:
logo
Tumbling Classes/ Cheer Classes/ Competitive Teams
4810 Mellway Ave., Torrance
brightlinespirit42.com
phone number

Target Market(s)

Teenagers and children ages 10-18 , parents of children ages 6-10 years

Industry/Entity Type

Gym

Requirements
Must have
• The photo attached. A catch word like "Soar" at the top. The text at the bottom should include logo, Tumbling Classes/ Cheer Classes/ Competitive Teams, 4810 Mellway Ave., Torrance, brightlinespirit42.com, (424)731-2649
Nice to have
• light to dark background
Should not have
• Not a lot of text

```html
<!DOCTYPE html>
<html lang="en">
<head>
<meta charset="utf-8">
<title>Soar – Brightline Spirit Poster</title>
<link rel="stylesheet" href="https://fonts.googleapis.com/css2?family=Arimo:wght@400;700&display=swap">
<style>
  :root {
    --sky: #b3caea;
    --sky-mid: #8d9fbd;
    --dusk: #4a4e5e;
    --night: #2b2a31;
    --ink: #1f1f22;
    --brand-teal: #1d5670;
    --accent-blue: #a9c6ea;
    --white: #ffffff;
  }
  html, body {
    margin: 0;
    padding: 0;
    width: 975px;
    height: 1200px;
    overflow: hidden;
    background: var(--night);
  }
  .poster {
    position: relative;
    width: 975px;
    height: 1200px;
    overflow: hidden;
    font-family: "Arimo", Arial, sans-serif;
    background: linear-gradient(180deg, var(--sky) 0%, var(--sky) 42%, var(--sky-mid) 62%, var(--dusk) 78%, var(--night) 100%);
  }
  .headline {
    position: absolute;
    top: 30px;
    left: 0;
    width: 100%;
    margin: 0;
    text-align: center;
    font-weight: 700;
    font-size: 118px;
    letter-spacing: -2px;
    color: var(--ink);
    line-height: 1;
  }
  .hero-photo {
    position: absolute;
    left: 230px;
    top: 170px;
    width: 470px;
    height: 830px;
    border-radius: 45% 45% 40% 40%;
    background: radial-gradient(ellipse at 50% 50%, rgba(138, 90, 60, 0.75) 0%, rgba(60, 50, 55, 0.55) 45%, rgba(179, 202, 234, 0) 75%);
  }
  .waves {
    position: absolute;
    inset: 0;
  }
  .class-list {
    position: absolute;
    top: 700px;
    right: 45px;
    margin: 0;
    padding: 0;
    list-style: none;
    text-align: right;
    color: var(--white);
    font-size: 25px;
    line-height: 46px;
  }
  .class-list li::before {
    content: "";
    display: inline-block;
    width: 11px;
    height: 11px;
    margin-right: 10px;
    border-radius: 50%;
    background: var(--white);
    vertical-align: middle;
  }
  .class-list li:nth-child(2) { margin-right: 55px; }
  .class-list li:nth-child(3) { margin-right: 100px; }
  .brand {
    position: absolute;
    top: 880px;
    right: 60px;
    display: flex;
    align-items: center;
    gap: 12px;
    font-size: 40px;
    font-weight: 700;
    color: var(--brand-teal);
  }
  .brand-dot {
    width: 20px;
    height: 20px;
    border-radius: 50%;
    background: var(--brand-teal);
  }
  .contact {
    position: absolute;
    top: 1000px;
    right: 115px;
    text-align: right;
    color: var(--white);
    font-size: 25px;
    line-height: 32px;
  }
  .contact p { margin: 0; }
  .call-to-action {
    position: absolute;
    bottom: 24px;
    left: 0;
    width: 100%;
    margin: 0;
    text-align: center;
    color: var(--accent-blue);
    font-size: 32px;
    line-height: 1.2;
  }
</style>
</head>
<body>
<main class="poster">
  <h1 class="headline">SOAR</h1>

  <div class="hero-photo" role="img" aria-label="Photo of a cheerleader in black athletic wear tucked mid-flip, upside down, with motion blur"></div>

  <svg class="waves" viewBox="0 0 975 1200" width="975" height="1200" aria-hidden="true">
    <path fill="var(--accent-blue)" d="M0 1060 C 300 1000 560 850 740 845 C 860 842 940 890 975 950 L975 1200 L0 1200 Z"/>
    <path fill="var(--white)" d="M0 1072 C 305 1012 565 862 742 858 C 860 855 935 900 975 962 L975 1200 L0 1200 Z"/>
    <path fill="var(--night)" d="M0 1118 C 340 1055 600 935 765 925 C 870 920 935 960 975 1010 L975 1200 L0 1200 Z"/>
  </svg>

  <ul class="class-list">
    <li>Tumbling Classes</li>
    <li>Cheer Classes</li>
    <li>Competitive Teams</li>
  </ul>

  <div class="brand">
    <span class="brand-name">Brightline Spirit</span>
    <span class="brand-dot"></span>
  </div>

  <div class="contact">
    <p>4810 Mellway Ave., Torrance</p>
    <p>www.brightlinespirit42.com</p>
  </div>

  <p class="call-to-action">For a free trial class CALL 424-731-2649 TODAY</p>
</main>
</body>
</html>
```